Sportdrink für Fussballer
Zielgruppe
WER WIR SIND?
Wir sind ein junges Label, das es sich zur Aufgabe macht, ambitionierte Fussballspieler aus dem Amateurbereich in Training & Spiel mit qualitativ hochwertiger Sportnahrung auszustatten.
Unsere Produkte richten sich an Sportler, die immer alles geben und mit unserer Unterstützung zu wahren Legenden auf dem Platz werden möchten.
Besucht auch gerne unseren Kickgram Channel: torheldwerk
ZIELGRUPPE?
- Ambitionierte Amateurfussballspieler und -spielerinnen
- Alter: 16 - 30
- Fitnessaffin / Gesundheits & Ernährungsbewusst
- Trendy / hipster
- Bewusstsein für Mode, Ästhetik, Nachhaltigkeit
Aufgabenstellung
Liebe Designer!
Für unser Produkt - ein isotonisches Getränkepulver - benötigen wir eure Expertise bei der Gestaltung eines ansprechenden Etiketts.
Unser Getränkepulver wird in Dosen mit einer Höhe von 12,5 cm und einem Durchmesser von 9 cm angeboten (siehe Anhang für Beispieldose).
Die exakten Maße zur Gestaltung des Etiketts können der beigefügten Druckstandsskizze entnommen werden ( 4 farbig, Chromolux 80g / qm).
1) Generelle Anmerkungen zum gewünschten Design:
- Unser Produkt richtet sich ausschließlich an die Zielgruppe "Fussballer"
- Das Etikett sollte stilistisch auf jeden Fall in die Richtung "handmade / handcrafted" gehen (siehe Beispiele)
- Das Etikett sollte möglichst clean sein und nur vereinzelte Farbelemente enthalten (idealerweise weißer oder schwarzer Hintergrund)
- Das Logo sollte das Kernelement des Etiketts sein (siehe Fox Hall)
- Zur Besseren Visualisierung sollte jedem 2D Entwurf auch ein 3D Entwurf beigefügt werden
2) Elemente auf der Vorderseite
- Logo (großflächige Darstellung) im "used-look" (abgesplittert, zerkratzt, etc…)
- Produktname: "Isotonisches Sportgetränk"
- Logos für folgende Produkteigenschaften:
o Echtes Fruchtpulver
o Keine künstlichen Zusatzstoffe
o Hergestellt in Deutschland
- Box oder Farbband für Geschmacksrichtung: "Zitrone/Limette" ( Sollte sich gut dafür eignen auch andere Geschmacksrichtungen darstellen zu können)
- Platzhalter für Grammangabe (200 bzw. 400 Gramm)
3) Elemente auf der Rückseite
- Text:
Die letzten Minuten laufen. Dein Wille ist ungebrochen aber jeder Sprint bringt deine Oberschenkel zum brennen. Du willst den Sieg, deine Muskeln nur noch die Eistonne. Laut einer Studie des KSV sind deine Energiereserven je nach Spielposition nach 60 bis 70 Minuten vollständig erschöpft.
Die Folgen:
x Unnötige Fehlpässe
x Fehlende Spritzigkeit

```html
<!DOCTYPE html>
<html lang="de">
<head>
<meta charset="utf-8">
<title>Torheldwerk – Isotonischer Sportdrink Etikett</title>
<link rel="stylesheet" href="https://fonts.googleapis.com/css2?family=Roboto+Condensed:wght@400;700&family=Saira+Condensed:wght@600;700&display=swap">
<style>
  :root {
    --label-black: #070707;
    --lime: #97c21f;
    --lime-line: #8cc21f;
    --white: #ffffff;
    --paper: #ffffff;
    --text-font: "Roboto Condensed", "Arial Narrow", sans-serif;
    --display-font: "Saira Condensed", "Arial Narrow", sans-serif;
  }
  * { margin: 0; padding: 0; box-sizing: border-box; }
  html, body { width: 1133px; height: 1200px; overflow: hidden; background: var(--paper); }
  .label {
    position: absolute; left: 20px; top: 371px; width: 1093px; height: 458px;
    background: var(--label-black); color: var(--white); font-family: var(--text-font);
  }
  .brand {
    position: absolute; left: 96px; top: 60px; width: 360px; text-align: center;
  }
  .brand-name {
    font-family: var(--text-font); font-weight: 700; font-size: 50px; letter-spacing: 1px;
    color: var(--white); line-height: 1; margin-top: 88px; text-transform: uppercase;
  }
  .brand-est { font-size: 10px; margin-top: 6px; letter-spacing: .5px; }
  .brand-est::before, .brand-est::after {
    content: ""; display: inline-block; width: 26px; height: 1px; background: var(--white);
    vertical-align: middle; margin: 0 6px;
  }
  .product-type {
    font-family: var(--display-font); font-weight: 700; color: var(--lime);
    font-size: 17px; line-height: 16px; letter-spacing: 1px; margin-top: 26px;
  }
  .claims { position: absolute; left: 522px; top: 34px; width: 93px; }
  .claim { position: relative; width: 93px; height: 82px; margin-bottom: 39px; }
  .claim svg { position: absolute; inset: 0; }
  .claim span {
    position: absolute; inset: 0; display: flex; align-items: center; justify-content: center;
    text-align: center; font-size: 11.5px; line-height: 15px; padding: 0 14px;
  }
  .info {
    position: absolute; left: 689px; top: 33px; width: 332px;
    font-size: 7.2px; line-height: 9.8px; text-align: justify;
  }
  .info p { margin-bottom: 8px; }
  .hl { color: var(--lime); }
  .symptoms { display: flex; justify-content: space-between; align-items: center; text-align: left; }
  .symptoms .dot {
    display: inline-block; width: 5px; height: 5px; border-radius: 50%; background: var(--lime);
  }
  .facts { position: relative; margin-bottom: 8px; text-align: left; }
  .facts .head { display: grid; grid-template-columns: 178px 90px 64px; }
  .facts .head span { color: var(--lime); }
  .facts .row { display: grid; grid-template-columns: 53px 113px 12px 79px 11px 64px; height: 10.4px; }
  .facts .row span { padding-left: 10px; }
  .facts .row .group { padding-left: 0; color: var(--lime); grid-column: 1; }
  .facts .row.fill .cell { background: var(--lime); }
  .facts .row .cell.v1 { grid-column: 4; padding-left: 0; }
  .facts .row .cell.v2 { grid-column: 6; padding-left: 0; }
  .facts .row .cell.name { grid-column: 2; }
  .imprint {
    position: absolute; left: 1046px; top: 385px; transform: rotate(-90deg); transform-origin: 0 0;
    font-size: 7.2px; white-space: nowrap; width: 275px;
  }
  .flavour-band {
    position: absolute; left: 0; right: 0; top: 397px; height: 27px; background: var(--lime);
  }
  .flavour {
    position: absolute; left: 96px; width: 360px; text-align: center; top: 3px;
    font-family: var(--display-font); font-weight: 700; font-size: 15px; letter-spacing: 1.5px;
  }
  .follow { position: absolute; left: 689px; top: 8px; font-size: 7.2px; }
  .web { position: absolute; left: 900px; width: 121px; text-align: right; top: 8px; font-size: 7.2px; }
</style>
</head>
<body>
<main class="label">
  <section class="brand">
    <div class="brand-name">Torheldwerk</div>
    <div class="brand-est">Est. 2017</div>
    <div class="product-type">ISOTONISCHER<br>SPORTDRINK</div>
  </section>

  <section class="claims">
    <div class="claim">
      <svg viewBox="0 0 93 82" width="93" height="82"><polygon points="22,1 71,1 92,41 71,81 22,81 1,41" fill="none" stroke="var(--lime-line)" stroke-width="1.2"/><polygon points="25,5 68,5 87,41 68,77 25,77 6,41" fill="none" stroke="var(--lime-line)" stroke-width="1"/></svg>
      <span>Echtes Fruchtpulver</span>
    </div>
    <div class="claim">
      <svg viewBox="0 0 93 82" width="93" height="82"><polygon points="22,1 71,1 92,41 71,81 22,81 1,41" fill="none" stroke="var(--lime-line)" stroke-width="1.2"/><polygon points="25,5 68,5 87,41 68,77 25,77 6,41" fill="none" stroke="var(--lime-line)" stroke-width="1"/></svg>
      <span>Ohne künstliche Zusatzstoffe</span>
    </div>
    <div class="claim">
      <svg viewBox="0 0 93 82" width="93" height="82"><polygon points="22,1 71,1 92,41 71,81 22,81 1,41" fill="none" stroke="var(--lime-line)" stroke-width="1.2"/><polygon points="25,5 68,5 87,41 68,77 25,77 6,41" fill="none" stroke="var(--lime-line)" stroke-width="1"/></svg>
      <span>Hergestellt in Deutschland</span>
    </div>
  </section>

  <section class="info">
    <p>Die letzten Minuten laufen. Dein Wille ist ungebrochen aber jeder Sprint bringt deine Oberschenkel zum brennen. Du willst den Sieg, deine Muskeln nur noch die Eistonne. Laut einer Studie des KSV sind deine Energiereserven je nach Spielposition nach 60 bis 70 Minuten vollständig erschöpft.&nbsp; Die Folgen:</p>
    <p class="symptoms"><span>Unnötige Fehlpässe</span><span class="dot"></span><span>Schwaches Zweikampfverhalten</span><span class="dot"></span><span>Fehlende Spritzigkeit</span><span class="dot"></span><span>Mangelnde Konzentration</span></p>
    <p>Um deine Speicher schnell wieder aufzuladen brauchst du Energie! Nachdem uns die üblichen Sportgetränke zu süß, bunt und künstlich waren, haben wir es uns zur Aufgabe gemacht, eine natürliche Alternative zu entwickeln. Dabei verzichten wir bewusst auf künstliche Farb-, Aroma- und Konservierungsstoffe und bedienen uns stattdessen nur an natürlichen Inhaltsstoffen. Als besonderes Highlight verarbeiten wir für unser Sportgetränk echte Früchte, die deinen Geschmacksknospen ein Grinsen ins Gesicht zaubern.</p>
    <p><span class="hl">Zubereitung- &amp; Verzehrempfehlung</span> Die Zubereitung ist easy: Je nach Vorliebe 24 g Pulver in 450 bis 550 ml Wasser geben, kräftig schütteln, fertig! Für eine optimale Flüssigkeits- und Energieversorgung in Training und Spiel empfehlen wir bereits beim Aufwärmen ca. 150 - 300 ml zu trinken. Während der Belastung sollte dann im Abstand von 15 Minuten ca. 150 ml getrunken werden.</p>

    <div class="facts">
      <div class="head"><span></span><span>pro Portion (24g)</span><span>pro 100g</span></div>
      <div class="row fill"><span class="group">Nährwerte</span><span class="cell name">Energie</span><span class="cell v1">336 kJ / 80 kcal</span><span class="cell v2">1334 kJ / 320 kcal</span></div>
      <div class="row"><span class="cell name">Fett</span><span class="cell v1">0 g</span><span class="cell v2">0 g</span></div>
      <div class="row fill"><span class="cell name">davon gesättigte Fettsäuren</span><span class="cell v1">0 g</span><span class="cell v2">0 g</span></div>
      <div class="row"><span class="cell name">Kohlenhydrate</span><span class="cell v1">21 g</span><span class="cell v2">84 g</span></div>
      <div class="row fill"><span class="cell name">davon Zucker</span><span class="cell v1">20 g</span><span class="cell v2">80 g</span></div>
      <div class="row"><span class="cell name">Eiweiss</span><span class="cell v1">0 g</span><span class="cell v2">0 g</span></div>
      <div class="row fill"><span class="cell name">Salz</span><span class="cell v1">900 mg</span><span class="cell v2">3600 mg</span></div>
    </div>
    <div class="facts">
      <div class="head"><span></span><span>pro Portion (24g)</span><span>in % NR?</span></div>
      <div class="row fill"><span class="group">Inhaltsstoffe</span><span class="cell name">Natrium</span><span class="cell v1">360 mg</span><span class="cell v2">15 %</span></div>
      <div class="row"><span class="cell name">Vitamin C</span><span class="cell v1">28 mg</span><span class="cell v2">35 %</span></div>
    </div>
    <p><span class="hl">Zutatenliste</span> Rohrzucker, Traubenzucker, Natriumcitrat, Zitronensäure, Magnesiumlactat, Calciumcitrat, Zitronensaft, Limettensaft, Kaliumcitrat, Ascorbinsäure (Vitamin C)</p>
    <p>Außerhalb der Reichweite von Kindern aufbewahren. Die empfohlene tägliche Verzehrmenge darf nicht überschritten werden. Nahrungsergänzungsmittel sollten nicht als Ersatz für eine ausgewogene und abwechslungsreiche Ernährung dienen. Kühl, trocken und dunkel aufbewahren.</p>
  </section>

  <div class="imprint">Vertrieb durch Feliks Brauner Sport Commerce, Am Sportpark 14, 20459 Hafenstadt</div>

  <footer class="flavour-band">
    <div class="flavour">Zitrone-Limette</div>
    <div class="follow">STAY TUNED und folge uns auf Kickgram, Teamfeed und im Web</div>
    <div class="web">www.torheldwerk.drink</div>
  </footer>
</main>
</body>
</html>
```